Math Word Problems Make Your Palms Sweat??

I need a landing page for lead magnet download and email capture. Prospects will get here from QV ad. Landing page should be clean, simple and aimed at parents of Algebra 1 students. I will attach logo. Please use logo brand colors and fonts. The final design should be clear, easy to understand with struggling students and parents that don't know how to help. Copy should include: (lead magnet download info:) Equation Riddle Rescue Bundle with examples AND solutions, Conquer word problems with a step by step guide written by former teacher and full time math tutor.

Target Market(s)

Parents of struggling high school math/Algebra 1 students

Colors
33b8a4
ffffff

Requirements
Must have
• address pain points of:
struggling students
word problems causing angst
parents not knowing how to help their child

be clean, simple and easy to see what my message is via copy, images and feel of page

brand colors (ffffff, 5f5e60, 00a99d)and fonts (questrial, glacial indifference and arimo) from attached logo

clear call to action (download the pdf/lead magnet)
Nice to have
• bulleted points, not too wordy but clear message

related images/teens/struggling with math

my headshot if it looks appropriate on page

(I will likely have revisions once I see the first draft)
Should not have
• crowded
hard to read
message hard to decipher
busy
unclear call to action

```html
<!DOCTYPE html>
<html lang="en">
<head>
<meta charset="utf-8">
<title>Clearpath Tutoring – Math Word Problems</title>
<link rel="stylesheet" href="https://fonts.googleapis.com/css2?family=Montserrat:wght@400;600;700;800&family=Questrial&display=swap">
<style>
:root{
  --teal:#33b8a4;
  --teal-deep:#00a99d;
  --ink:#2d2d2f;
  --grey:#5f5e60;
  --light:#f1f4f9;
  --white:#ffffff;
  --dark:#332f2e;
  --pink:#c2185b;
  --ribbon:#7cc84a;
  --sky:#bfe3f4;
  --violet:#5b6ee1;
}
*{box-sizing:border-box;margin:0;padding:0}
html,body{width:1200px;height:3300px;overflow:hidden}
body{font-family:"Questrial",sans-serif;color:var(--grey);background:var(--white);position:relative}
h1,h2,h3,.btn,.nav a,.brand{font-family:"Montserrat",sans-serif}
.btn{display:inline-block;background:var(--dark);color:var(--white);font-size:12px;font-weight:700;letter-spacing:1.5px;text-transform:uppercase;padding:12px 30px;border-radius:22px;white-space:nowrap}

/* header */
.site-header{position:absolute;top:0;left:0;width:1200px;height:100px;display:flex;align-items:center;justify-content:space-between;padding:0 160px}
.brand{display:flex;align-items:center;gap:10px;font-weight:700;font-size:26px;color:var(--teal-deep)}
.brand-mark{width:22px;height:22px;background:var(--teal-deep)}
.nav{display:flex;gap:28px}
.nav a{font-size:13px;color:var(--grey);text-decoration:none;letter-spacing:1px;font-weight:600}
.nav a.active{color:var(--teal-deep)}

/* hero */
.hero{position:absolute;top:100px;left:0;width:1200px;height:420px;background:linear-gradient(90deg,#2aa893 0%,#39b9a6 55%,#5fc6b5 100%);clip-path:polygon(0 0,100% 0,100% 78%,0 100%)}
.hero-photo{position:absolute;right:0;top:0;width:560px;height:100%;background:linear-gradient(90deg,rgba(255,255,255,0) 0%,rgba(220,240,236,.35) 60%,rgba(240,220,200,.45) 100%)}
.hero-copy{position:absolute;left:205px;top:95px;width:400px;color:var(--white)}
.hero-copy .kicker{font-family:"Montserrat",sans-serif;font-size:40px;font-weight:700;line-height:1}
.hero-copy h1{font-size:64px;font-weight:800;line-height:1.05;letter-spacing:1px}
.hero-copy p{font-size:15px;line-height:1.45;margin:14px 0 22px}

/* about */
.about{position:absolute;top:600px;left:0;width:1200px;height:360px}
.about-frame{position:absolute;left:252px;top:30px;width:280px;height:330px;background:var(--teal)}
.about-photo{position:absolute;left:228px;top:12px;width:280px;height:330px;background:linear-gradient(160deg,#d9d2c8 0%,#b9a898 55%,#8a7b6f 100%);box-shadow:0 6px 16px rgba(0,0,0,.15)}
.about-copy{position:absolute;left:605px;top:38px;width:370px}
.about-copy h2{font-size:30px;font-weight:700;color:var(--teal-deep);letter-spacing:1px}
.about-copy .rule{width:40px;height:3px;background:var(--teal);margin:8px 0 16px}
.about-copy p{font-size:14px;line-height:1.55;margin-bottom:14px}

/* pain points band */
.pain{position:absolute;top:1100px;left:0;width:1200px;height:440px;background:var(--teal);color:var(--white);text-align:center}
.pain h2{padding-top:56px;font-size:24px;font-weight:700;letter-spacing:1px}
.pain h2 span{display:block;font-size:30px}
.points{display:flex;justify-content:center;gap:60px;margin-top:60px;text-align:left}
.point{width:220px}
.point svg{display:block;margin-bottom:16px}
.point h3{font-size:24px;font-weight:700;margin-bottom:8px}
.point p{font-size:14px;line-height:1.45}

/* video */
.video{position:absolute;top:1540px;left:0;width:1200px;height:580px;background:linear-gradient(180deg,#e4e4e2 0%,#cfcfcc 62%,#b7a593 62%,#9b8670 100%)}
.video-card{position:absolute;left:280px;top:52px;width:632px;height:500px;background:var(--white);padding:32px 34px;text-align:center;box-shadow:0 8px 24px rgba(0,0,0,.18)}
.video-card h2{font-size:30px;font-weight:700;color:var(--ink);line-height:1.2}
.video-card h2 em{font-style:normal;color:var(--teal-deep)}
.video-card p{font-size:13px;line-height:1.45;margin:12px 18px 18px}
.video-frame{position:relative;height:320px;background:linear-gradient(135deg,#7e5a3c 0%,#c39a5e 50%,#e3c891 100%)}
.play{position:absolute;left:50%;top:60%;transform:translate(-50%,-50%)}

/* pricing */
.pricing{position:absolute;top:2120px;left:0;width:1200px;height:560px;background:var(--light);text-align:center}
.pricing h2{padding-top:48px;font-size:30px;font-weight:700;color:var(--ink);letter-spacing:1px}
.deco{position:absolute}
.plans{position:absolute;left:228px;top:150px;width:744px;display:flex;justify-content:space-between;align-items:flex-start}
.plan{position:relative;width:222px;background:var(--white);padding:30px 20px;box-shadow:0 6px 20px rgba(0,0,0,.08);overflow:hidden}
.plan.featured{width:232px;margin-top:-30px;padding:44px 20px 40px}
.plan h3{font-size:13px;font-weight:700;color:var(--ink);margin:10px 0 12px}
.price{font-family:"Montserrat",sans-serif;font-size:34px;font-weight:700;color:var(--teal-deep)}
.price small{font-size:10px;color:var(--grey);font-weight:400}
.plan ul{list-style:none;font-size:12px;line-height:2.1;margin:12px 0 18px}
.plan .btn{font-size:10px;padding:9px 22px}
.ribbon{position:absolute;left:0;top:0;width:0;height:0;border-top:56px solid var(--ribbon);border-right:56px solid transparent}

/* lead capture */
.contact{position:absolute;top:2680px;left:0;width:1200px;height:520px;background:linear-gradient(135deg,#d8c6a6 0%,#b7a78b 40%,#8fa5b4 100%)}
.contact-card{position:absolute;left:400px;top:72px;width:400px;height:428px;background:var(--white);box-shadow:0 8px 24px rgba(0,0,0,.18);text-align:center}
.contact-card h2{background:var(--teal);color:var(--white);font-size:26px;font-weight:700;padding:16px 0;letter-spacing:1px}
.contact-card .lead{font-size:15px;color:var(--ink);margin:18px 40px 16px;line-height:1.35}
.field{width:290px;height:34px;margin:0 auto 12px;background:#eef0f3;border-radius:4px;text-align:left;padding:9px 14px;font-size:12px;color:#8b8a8c}
.contact-card .btn{margin-top:6px;width:290px;font-size:11px}

/* footer */
.site-footer{position:absolute;top:3200px;left:0;width:1200px;height:100px;background:var(--dark);color:#d8d8d8;font-size:13px;letter-spacing:1px;display:flex;align-items:center;justify-content:center}
</style>
</head>
<body>

<header class="site-header">
  <div class="brand"><span class="brand-mark"></span>Clearpath Tutoring</div>
  <nav class="nav">
    <a class="active">HOME</a><a>SIGN UP</a><a>REGISTER</a><a>CONTACT</a>
  </nav>
</header>

<section class="hero">
  <div class="hero-photo" role="img" aria-label="Photo of a young student in front of a chalkboard full of math equations"></div>
  <div class="hero-copy">
    <div class="kicker">Math Problem?</div>
    <h1>WORRIED</h1>
    <p>Get the free Equation Riddle Rescue Bundle: examples AND solutions from a former teacher and full time math tutor.</p>
    <span class="btn">Download Free PDF</span>
  </div>
</section>

<section class="about">
  <div class="about-frame"></div>
  <div class="about-photo" role="img" aria-label="Headshot of the tutor, a smiling woman with glasses"></div>
  <div class="about-copy">
    <h2>ABOUT TEACHER</h2>
    <div class="rule"></div>
    <p>Does your teen freeze when a word problem shows up? I spent years in the classroom and now tutor full time, helping students turn confusing sentences into clear equations they can solve.</p>
    <p>My approach is simple: read, picture, write, solve and check. Parents get the same tools, so you can finally help at the kitchen table without guessing.</p>
    <span class="btn">More About Me</span>
  </div>
</section>

<section class="pain">
  <h2>MATH WORD PROBLEMS <span>MAKE YOUR PALMS SWEAT??</span></h2>
  <div class="points">
    <div class="point">
      <svg width="44" height="44" viewBox="0 0 44 44"><circle cx="22" cy="22" r="19" fill="none" stroke="#fff" stroke-width="3"/><path d="M13 22l6 6 12-13" fill="none" stroke="#fff" stroke-width="3.5" stroke-linecap="round" stroke-linejoin="round"/></svg>
      <h3>Basic Training</h3>
      <p>Learn to spot the key words, name the unknown and build the equation one calm step at a time.</p>
    </div>
    <div class="point">
      <svg width="44" height="44" viewBox="0 0 44 44"><circle cx="22" cy="22" r="19" fill="none" stroke="#fff" stroke-width="3"/><path d="M13 22l6 6 12-13" fill="none" stroke="#fff" stroke-width="3.5" stroke-linecap="round" stroke-linejoin="round"/></svg>
      <h3>Specail Coaching</h3>
      <p>Worked examples with full solutions show exactly where each number goes and why the answer makes sense.</p>
    </div>
    <div class="point">
      <svg width="44" height="44" viewBox="0 0 44 44"><circle cx="22" cy="22" r="19" fill="none" stroke="#fff" stroke-width="3"/><path d="M13 22l6 6 12-13" fill="none" stroke="#fff" stroke-width="3.5" stroke-linecap="round" stroke-linejoin="round"/></svg>
      <h3>Help Parents</h3>
      <p>Clear guides give parents plain language tips so homework time stops turning into a battle.</p>
    </div>
  </div>
</section>

<section class="video" role="img" aria-label="Background photo of a white brick wall above a wooden floor">
  <div class="video-card">
    <h2>WATCH OUR COURSES VIDEO<br>IN <em>LIVE ACTION</em></h2>
    <p>See one word problem from the free bundle read, broken down and solved step by step, start to finish.</p>
    <div class="video-frame" role="img" aria-label="Video still of an instructor presenting an online course">
      <svg class="play" width="60" height="42" viewBox="0 0 60 42"><rect width="60" height="42" rx="10" fill="#222" opacity=".85"/><path d="M24 12l14 9-14 9z" fill="#fff"/></svg>
    </div>
  </div>
</section>

<section class="pricing">
  <h2>AFORDABLE PRICE</h2>
  <svg class="deco" style="left:72px;top:262px" width="22" height="22" viewBox="0 0 22 22"><path d="M2 2l18 9-18 9z" fill="none" stroke="var(--violet)" stroke-width="2"/></svg>
  <svg class="deco" style="left:1060px;top:222px" width="40" height="40"><circle cx="20" cy="20" r="18" fill="var(--sky)"/></svg>
  <svg class="deco" style="left:160px;top:230px" width="10" height="10"><circle cx="5" cy="5" r="4" fill="var(--pink)"/></svg>
  <svg class="deco" style="left:1070px;top:300px" width="10" height="10"><circle cx="5" cy="5" r="4" fill="var(--pink)"/></svg>
  <svg class="deco" style="left:130px;top:330px" width="18" height="18"><circle cx="9" cy="9" r="7" fill="var(--sky)"/></svg>
  <div class="plans">
    <div class="plan">
      <svg width="34" height="30" viewBox="0 0 34 30"><path d="M2 4h13l2 2 2-2h13v22H19l-2 2-2-2H2z" fill="var(--pink)"/><path d="M17 6v20" stroke="#fff" stroke-width="1.5"/></svg>
      <h3>Personal</h3>
      <div class="price">25$ <small>/month</small></div>
      <ul><li>Step by step guide</li><li>Worked examples</li><li>Full solutions</li><li>First 30 days free</li></ul>
      <span class="btn">Learn More</span>
    </div>
    <div class="plan featured">
      <div class="ribbon"></div>
      <svg width="34" height="30" viewBox="0 0 34 30"><path d="M2 4h13l2 2 2-2h13v22H19l-2 2-2-2H2z" fill="var(--pink)"/><path d="M17 6v20" stroke="#fff" stroke-width="1.5"/></svg>
      <h3>Business</h3>
      <div class="price">29$ <small>/month</small></div>
      <ul><li>Step by step guide</li><li>Worked examples</li><li>Full solutions</li><li>Weekly practice sets</li><li>First 30 days free</li></ul>
      <span class="btn">Learn More</span>
    </div>
    <div class="plan">
      <svg width="34" height="30" viewBox="0 0 34 30"><path d="M2 4h13l2 2 2-2h13v22H19l-2 2-2-2H2z" fill="var(--pink)"/><path d="M17 6v20" stroke="#fff" stroke-width="1.5"/></svg>
      <h3>Ultimate</h3>
      <div class="price">50$ <small>/month</small></div>
      <ul><li>Step by step guide</li><li>Worked examples</li><li>Full solutions</li><li>Weekly practice sets</li><li>First 30 days free</li></ul>
      <span class="btn">Learn More</span>
    </div>
  </div>
</section>

<section class="contact" role="img" aria-label="Background photo of students raising hands in a classroom">
  <div class="contact-card">
    <h2>CONTACT US</h2>
    <div class="lead">Enter your info to get the free Equation Riddle Rescue Bundle PDF</div>
    <div class="field">First Name</div>
    <div class="field">Last Name</div>
    <div class="field">Phone Number</div>
    <div class="field">Email</div>
    <span class="btn">Download the Free PDF</span>
  </div>
</section>

<footer class="site-footer">COPYRIGHT 2020, ALL RIGHTS RESERVED</footer>

</body>
</html>
```